Flyers

Modify Existing Flyer and create another for exterior company
Updates

Previous Brief has been updated- we want to update this existing one also

Target Market(s)

Exterior Remodeling Customers

Industry/Entity Type

Remodeling/Construction

```html
<!DOCTYPE html>
<html lang="en">
<head>
<meta charset="utf-8">
<title>Hearthline Renovation – Remodeling Flyer</title>
<link rel="stylesheet" href="https://fonts.googleapis.com/css2?family=Poppins:wght@400;500;600;700&display=swap">
<style>
:root{
  --navy:#0b1428;
  --navy-2:#111c36;
  --blue:#0a74c9;
  --blue-bright:#1283db;
  --orange:#ea5a1c;
  --ink:#1d1f26;
  --muted:#3a3d45;
  --paper:#ffffff;
  --stage:#eceef1;
  --rule:#c9ccd3;
}
*{box-sizing:border-box;margin:0;padding:0}
html,body{width:1200px;height:2767px;overflow:hidden}
body{background:var(--stage);font-family:"Poppins",sans-serif;color:var(--ink);position:relative}
.flyer{position:absolute;left:0;top:534px;width:1200px;height:1698px;background:var(--paper);overflow:hidden;box-shadow:0 10px 30px rgba(0,0,0,.18)}
.abs{position:absolute}
.header-band{left:0;top:0;width:1200px;height:258px;background:linear-gradient(180deg,var(--navy) 0%,var(--navy-2) 100%)}
.side-stripe{top:258px;width:56px;height:36px;background:var(--blue-bright)}
.side-stripe.left{left:0}.side-stripe.right{right:0}
.brand{left:0;top:62px;width:1200px;text-align:center;font-family:"Poppins",sans-serif;font-weight:500;font-size:32px;letter-spacing:.5px;color:#ffffff}
.hero{left:56px;top:160px;width:1088px;height:298px;background:#fff;padding:6px}
.hero-photo{position:absolute;top:6px;bottom:6px}
.hero-bath{left:6px;width:560px;background:linear-gradient(160deg,#f2f1ee 0%,#d9d6d0 55%,#8d8a85 100%)}
.hero-kitchen{right:6px;width:560px;background:linear-gradient(170deg,#c9d3dc 0%,#aebfcd 50%,#8d7a62 100%);clip-path:polygon(60px 0,100% 0,100% 100%,0 100%)}
.hero-label{position:absolute;bottom:6px;height:56px;color:#fff;font-weight:600;font-size:36px;line-height:56px;letter-spacing:.5px}
.hero-label.bath{left:6px;width:560px;background:rgba(20,24,34,.72);padding-left:118px}
.hero-label.kitchen{right:6px;width:580px;background:var(--orange);clip-path:polygon(28px 0,100% 0,100% 100%,0 100%);padding-left:240px}
.headline{left:0;top:462px;width:1200px;text-align:center;font-weight:600;font-size:46px;line-height:54px;color:var(--ink)}
.headline-accent{left:0;top:512px;width:1200px;text-align:center;font-weight:700;font-size:54px;line-height:60px;color:var(--blue)}
.tagline{left:82px;top:578px;width:846px;height:38px;background:var(--orange);color:#fff;font-weight:600;font-size:24px;line-height:38px;padding-left:18px;letter-spacing:.3px;clip-path:polygon(0 0,100% 0,calc(100% - 14px) 100%,0 100%)}
.location{left:932px;top:578px;width:190px;height:38px;background:var(--navy);color:#fff;font-weight:600;font-size:15px;line-height:38px;border-radius:20px 0 0 20px;padding-left:20px;display:flex;align-items:center;gap:8px;white-space:nowrap}
.divider{left:82px;width:1038px;height:0;border-top:2px dotted var(--rule)}
.service-title{font-weight:600;font-size:38px;line-height:44px;color:var(--ink);white-space:nowrap}
.service-title .accent{color:var(--blue)}
.service-desc{font-weight:500;font-size:16.5px;line-height:20px;color:var(--ink)}
.checklist{list-style:none;font-size:15.5px;line-height:26px;color:var(--muted)}
.checklist li{position:relative;padding-left:24px;white-space:nowrap}
.checklist li::before{content:"";position:absolute;left:2px;top:8px;width:10px;height:10px;border:1.5px solid var(--orange);border-radius:50%}
.checklist li::after{content:"";position:absolute;left:6px;top:10px;width:3px;height:5px;border:solid var(--orange);border-width:0 1.5px 1.5px 0;transform:rotate(40deg)}
.photo{border:1px solid #d8dade}
.icon{width:52px;height:52px}
.footer-blue{left:0;top:1619px;width:1200px;height:79px;background:var(--blue-bright)}
.footer-orange{left:0;top:1614px;width:470px;height:84px;background:var(--orange);clip-path:polygon(0 0,100% 0,calc(100% - 22px) 100%,0 100%)}
.footer-cut{left:448px;top:1614px;width:30px;height:84px;background:#fff;clip-path:polygon(22px 0,30px 0,8px 100%,0 100%)}
.cta-small{left:80px;top:1622px;font-weight:500;font-size:27px;line-height:32px;color:#fff}
.cta-big{left:80px;top:1650px;font-weight:700;font-size:41px;line-height:44px;color:#fff}
.contact{top:1636px;font-weight:600;font-size:28px;line-height:44px;color:#fff;display:flex;align-items:center;gap:8px;white-space:nowrap}
</style>
</head>
<body>
<main class="flyer">
  <div class="abs header-band"></div>
  <div class="abs side-stripe left"></div>
  <div class="abs side-stripe right"></div>
  <div class="abs brand">Hearthline Renovation</div>

  <section class="abs hero">
    <div class="hero-photo hero-bath" role="img" aria-label="Bright white bathroom with freestanding tub, window and potted plants"></div>
    <div class="hero-photo hero-kitchen" role="img" aria-label="Pale blue kitchen with island, pendant lamps and bar stools"></div>
    <div class="hero-label bath">BATHROOM</div>
    <div class="hero-label kitchen">KITCHEN</div>
  </section>

  <h1 class="abs headline">READY FOR A BEAUTIFUL AND FUNCTIONAL</h1>
  <h2 class="abs headline-accent">KITCHEN OR BATHROOM?</h2>
  <div class="abs tagline">WORK WITH A TOP-RATED LOCAL REMODELING COMPANY IN</div>
  <div class="abs location">
    <svg width="16" height="18" viewBox="0 0 18 20" fill="none" stroke="#fff" stroke-width="2"><path d="M9 18s6-6 6-10a6 6 0 0 0-12 0c0 4 6 10 6 10z"/><circle cx="9" cy="8" r="2"/><path d="M3 19h12"/></svg>
    BROOKVALE, IA
  </div>

  <svg class="abs icon" style="left:82px;top:650px" viewBox="0 0 52 52" fill="none" stroke-width="2.5"><rect x="4" y="26" width="44" height="22" stroke="#0a74c9"/><path d="M4 36h44M20 26v22M30 10v16M36 6v20" stroke="#0a74c9"/><rect x="8" y="8" width="14" height="10" stroke="#ea5a1c"/><path d="M10 42h6M24 31h20" stroke="#ea5a1c"/></svg>
  <h3 class="abs service-title" style="left:148px;top:648px">KITCHEN <span class="accent">REMODELING</span></h3>
  <p class="abs service-desc" style="left:152px;top:696px;width:570px">Whatever your vision is for your new kitchen, our crew can help you<br>bring it to life. You can trust us for :</p>
  <ul class="abs checklist" style="left:150px;top:744px">
    <li>Open concept design services</li>
    <li>Kitchen cabinet installation services</li>
    <li>Kitchen countertop installation services</li>
    <li>Tile installation services</li>
    <li>Lighting installation services</li>
  </ul>
  <ul class="abs checklist" style="left:506px;top:744px">
    <li>Plumbing upgrade services</li>
    <li>Electrical upgrade services</li>
    <li>Drywall services</li>
    <li>Painting services</li>
  </ul>
  <div class="abs photo" style="left:757px;top:650px;width:363px;height:203px;background:linear-gradient(160deg,#3a4a62 0%,#4c5d76 45%,#8a6a4a 100%)" role="img" aria-label="Dark blue kitchen with dining table, chairs and a large potted plant"></div>
  <div class="abs divider" style="top:877px"></div>

  <div class="abs photo" style="left:82px;top:889px;width:363px;height:202px;background:linear-gradient(150deg,#eeebe6 0%,#c8c3b8 45%,#5e7a52 100%)" role="img" aria-label="Modern bathroom with freestanding tub facing a window onto garden greenery"></div>
  <svg class="abs icon" style="left:466px;top:912px" viewBox="0 0 52 52" fill="none" stroke-width="2.5"><rect x="4" y="6" width="18" height="14" stroke="#ea5a1c"/><path d="M6 26h22v8a8 8 0 0 1-8 8h-6a8 8 0 0 1-8-8z" stroke="#0a74c9"/><path d="M34 18h14v12H34zM36 30v16h10V30" stroke="#0a74c9"/><path d="M10 42v6M22 42v6" stroke="#0a74c9"/></svg>
  <h3 class="abs service-title" style="left:529px;top:910px">BATHROOM <span class="accent">REMODELING</span></h3>
  <p class="abs service-desc" style="left:531px;top:955px;width:600px">When you hire us for your bathroom remodeling project, the possibilities are endless. Our experienced and talented team can :</p>
  <ul class="abs checklist" style="left:526px;top:1008px">
    <li>Install a custom tile shower</li>
    <li>Build a new vanity</li>
  </ul>
  <ul class="abs checklist" style="left:786px;top:1008px">
    <li>Install flooring and tile</li>
    <li>Replace your plumbing and light fixtures</li>
  </ul>
  <div class="abs divider" style="top:1102px"></div>

  <svg class="abs icon" style="left:82px;top:1147px" viewBox="0 0 52 52" fill="none" stroke-width="2.5"><path d="M6 20a20 12 0 0 1 40 0z" stroke="#ea5a1c"/><path d="M26 8v40" stroke="#ea5a1c"/><path d="M4 34h44M10 34v14M42 34v14M8 42h36" stroke="#0a74c9"/></svg>
  <h3 class="abs service-title" style="left:147px;top:1150px">DECKS/<span class="accent">PATIOS</span></h3>
  <p class="abs service-desc" style="left:90px;top:1196px;width:640px">An outdoor space is a great addition to any residential property. When you decide to build a patio or deck, you'll be able to experience a variety of benefits. Your outdoor area will increase your :</p>
  <ul class="abs checklist" style="left:86px;top:1272px;display:flex;gap:16px">
    <li>Property value</li>
    <li>Curb appeal</li>
    <li>Functional living space</li>
  </ul>
  <div class="abs photo" style="left:757px;top:1115px;width:363px;height:203px;background:linear-gradient(170deg,#cdd3cf 0%,#8f8a78 45%,#5c7a84 75%,#7f7466 100%)" role="img" aria-label="Backyard patio with pool, lounge chairs, umbrellas and a stone cottage"></div>
  <div class="abs divider" style="top:1330px"></div>

  <div class="abs photo" style="left:82px;top:1347px;width:363px;height:203px;background:linear-gradient(165deg,#e8e2d6 0%,#b59e7e 45%,#4a3d30 100%)" role="img" aria-label="Spacious bedroom with large bed, armchair and floor-to-ceiling windows"></div>
  <svg class="abs icon" style="left:507px;top:1350px" viewBox="0 0 52 52" fill="none" stroke-width="2.5"><path d="M4 26L22 10l18 16" stroke="#ea5a1c"/><path d="M10 22v24h24V22" stroke="#ea5a1c"/><rect x="18" y="30" width="8" height="8" stroke="#ea5a1c"/><path d="M34 30h14v16H34" stroke="#0a74c9"/><path d="M41 34v8M37 38h8" stroke="#0a74c9"/></svg>
  <h3 class="abs service-title" style="left:575px;top:1353px">HOME <span class="accent">ADDITIONS</span></h3>
  <p class="abs service-desc" style="left:577px;top:1398px;width:560px">No matter what kind of space you need, our team will bring your vision to life. You can hire us if you need a :</p>
  <ul class="abs checklist" style="left:574px;top:1449px">
    <li>Bathroom addition</li>
    <li>Bedroom addition</li>
    <li>Garage addition</li>
    <li>Basement addition</li>
  </ul>
  <ul class="abs checklist" style="left:810px;top:1449px">
    <li>Guest room addition</li>
    <li>Living room addition</li>
    <li>Sunroom addition</li>
  </ul>

  <div class="abs footer-blue"></div>
  <div class="abs footer-orange"></div>
  <div class="abs footer-cut"></div>
  <div class="abs cta-small">CALL TODAY FOR YOUR</div>
  <div class="abs cta-big">FREE ESTIMATE</div>
  <div class="abs contact" style="left:500px">
    <svg width="24" height="24" viewBox="0 0 24 24" fill="#fff"><path d="M6.6 10.8a15 15 0 0 0 6.6 6.6l2.2-2.2a1 1 0 0 1 1-.25 11.4 11.4 0 0 0 3.6.57 1 1 0 0 1 1 1V20a1 1 0 0 1-1 1A17 17 0 0 1 3 4a1 1 0 0 1 1-1h3.5a1 1 0 0 1 1 1c0 1.25.2 2.45.57 3.57a1 1 0 0 1-.25 1z"/></svg>
    555-014-2290
  </div>
  <div class="abs contact" style="left:760px">
    <svg width="24" height="24" viewBox="0 0 24 24" fill="none" stroke="#fff" stroke-width="2"><circle cx="12" cy="12" r="9"/><path d="M3 12h18M12 3c3 3 3 15 0 18M12 3c-3 3-3 15 0 18"/></svg>
    www.hearthlinereno.com
  </div>
</main>
</body>
</html>
```